Tarnby Group letterhead

Hi,

I need a letterhead template created for our business. This should be done in word format and A4 size. The images need to not move in the template ie when I am adding writing in etc. and should flow on when I get to a second page.

I have attached our logo templates below.

Other details to include on the letterhead somewhere are:

0438 915 267
Max@Tarnbyelectrical.example.au
PO Box 817 Marrowvale NSW 2190
ABN: 57 318 962 407

Thanks!

```html
<!DOCTYPE html>
<html lang="en">
<head>
<meta charset="utf-8">
<title>Tarnby Group Letterhead</title>
<link rel="stylesheet" href="https://fonts.googleapis.com/css2?family=Roboto:wght@400;700&display=swap">
<style>
  :root {
    --brand-orange: #f15a29;
    --ink: #111111;
    --paper: #ffffff;
  }
  html, body {
    margin: 0;
    padding: 0;
    width: 927px;
    height: 1200px;
    overflow: hidden;
    background: var(--paper);
  }
  .letterhead {
    position: relative;
    width: 927px;
    height: 1200px;
    background: var(--paper);
    font-family: "Roboto", Arial, sans-serif;
    color: var(--ink);
  }
  .frame {
    position: absolute;
    inset: 0;
    width: 927px;
    height: 1200px;
  }
  .frame .band { fill: var(--brand-orange); }
  .frame .gap { fill: var(--paper); }
  .brand {
    position: absolute;
    top: 62px;
    left: 650px;
    width: 220px;
    text-align: center;
  }
  .brand-mark {
    display: block;
    margin: 0 auto 10px;
    width: 58px;
    height: 58px;
    border-radius: 50%;
    background: var(--ink);
  }
  .brand-name {
    font-size: 22px;
    font-weight: 700;
    letter-spacing: 0.5px;
    text-transform: uppercase;
    color: var(--ink);
  }
  .letter-body {
    position: absolute;
    top: 432px;
    left: 136px;
    width: 700px;
    margin: 0;
    font-size: 18px;
    line-height: 24.7px;
  }
  .contact {
    position: absolute;
    top: 1046px;
    left: 68px;
    margin: 0;
    font-size: 17px;
    line-height: 21.7px;
  }
</style>
</head>
<body>
<div class="letterhead">
  <svg class="frame" viewBox="0 0 612 792" preserveAspectRatio="none" aria-hidden="true">
    <!-- top band -->
    <polygon class="band" points="200,0 612,0 612,26 226,26"/>
    <polygon class="gap" points="222,0 230,0 256,26 248,26"/>
    <polygon class="gap" points="246,0 254,0 280,26 272,26"/>
    <!-- right band -->
    <polygon class="band" points="586,250 612,276 612,410 586,410"/>
    <polygon class="gap" points="586,272 612,298 612,306 586,280"/>
    <polygon class="gap" points="586,296 612,322 612,330 586,304"/>
    <!-- left band -->
    <polygon class="band" points="0,200 26,226 26,792 0,792"/>
    <polygon class="gap" points="0,222 26,248 26,256 0,230"/>
    <polygon class="gap" points="0,246 26,272 26,280 0,254"/>
    <!-- bottom band -->
    <polygon class="band" points="0,766 612,766 612,792 0,792"/>
    <polygon class="gap" points="452,766 460,766 486,792 478,792"/>
    <polygon class="gap" points="476,766 484,766 510,792 502,792"/>
    <polygon class="gap" points="500,766 508,766 534,792 526,792"/>
  </svg>

  <header class="brand">
    <span class="brand-mark"></span>
    <div class="brand-name">Tarnby Group</div>
  </header>

  <p class="letter-body">
    Lorem ipsum dolor sit amet, consectetur adipiscing elit.<br>
    Pellentesque id libero bibendum, ultrices neque placerat, condimentum metus.<br>
    Nunc rhoncus est aliquam urna finibus, eget imperdiet velit varius.<br>
    Etiam ornare ligula at viverra mollis.<br>
    Maecenas scelerisque massa ac tortor bibendum, eget luctus nunc aliquam.<br>
    Maecenas auctor lacus eget ornare elementum.<br>
    Suspendisse sed augue quis urna malesuada ultricies ac ut nunc.<br>
    Morbi suscipit justo a viverra pretium.<br>
    Praesent a leo non orci tempus imperdiet.<br>
    Proin sit amet mi nec ante laoreet sollicitudin eget in lacus.<br>
    Cras malesuada eros vitae luctus pellentesque.<br>
    Maecenas a nunc sagittis eros dapibus condimentum.<br>
    In volutpat sapien vel lorem pharetra, vitae luctus dolor feugiat.<br>
    Sed sollicitudin metus sit amet risus tristique pretium.<br>
    Integer id nunc et eros mattis varius.<br>
    Praesent mollis erat id orci dictum feugiat.
  </p>

  <address class="contact" style="font-style: normal;">
    0438 915 267<br>
    Max@Tarnbyelectrical.example.au<br>
    PO Box 817 Marrowvale NSW 2190<br>
    ABN: 57 318 962 407
  </address>
</div>
</body>
</html>
```